Tidewell Grove Vitamin C Serum

We need a product label and box designed for our Vitamin C Serum product. The label will go on a 2oz bottle and the box will hold the 2oz bottle. Attached are the box and label templates as well as a Vitamin C Serum we have with another brand.

For this brand, we're looking to have the product look high end/luxury.

Target Market(s)

40+ year old women

```html
<!DOCTYPE html>
<html lang="en">
<head>
<meta charset="UTF-8">
<title>Tidewell Grove Vitamin C Facial Serum – Box and Label</title>
<link href="https://fonts.googleapis.com/css2?family=Jost:wght@400;500;600&family=Oswald:wght@300;400&display=swap" rel="stylesheet">
<style>
  :root {
    --backdrop: #fcd3d9;
    --orange: #ef7532;
    --orange-deep: #d9652a;
    --gold: #c8962a;
    --gold-light: #d9ac2c;
    --label-gold: #f4b82a;
    --ink: #2f2f2f;
    --pill-text: #fde3cf;
    --panel-light: #ffffff;
    --panel-silver: #c9c9c9;
  }
  * { margin: 0; padding: 0; box-sizing: border-box; }
  html, body {
    width: 1200px;
    height: 800px;
    overflow: hidden;
    background: var(--backdrop);
    font-family: "Jost", sans-serif;
    color: var(--ink);
  }
  .artboard {
    position: relative;
    width: 1200px;
    height: 800px;
    display: flex;
    align-items: center;
    justify-content: center;
    gap: 70px;
  }

  /* ---------- Box front panel ---------- */
  .box-front {
    width: 240px;
    height: 712px;
    display: flex;
    flex-direction: column;
    background: linear-gradient(160deg, var(--panel-light) 0%, #f4f4f4 35%, #dedede 70%, var(--panel-silver) 100%);
  }
  .band { background: var(--orange); flex: none; }
  .box-front .band { height: 18px; }
  .box-front .band--bottom { background: linear-gradient(90deg, var(--orange-deep), var(--orange)); }
  .box-body {
    flex: 1;
    display: flex;
    flex-direction: column;
    align-items: center;
    padding: 0 14px;
  }

  .brand {
    display: flex;
    flex-direction: column;
    align-items: center;
    justify-content: center;
    gap: 12px;
  }
  .brand-dot {
    border-radius: 50%;
    background: var(--orange);
  }
  .brand-name {
    font-weight: 500;
    color: var(--ink);
    letter-spacing: 0.02em;
    white-space: nowrap;
  }

  .product-title {
    font-weight: 500;
    line-height: 1;
    letter-spacing: -0.01em;
    white-space: nowrap;
  }
  .product-pill {
    background: var(--orange);
    border-radius: 6px;
    color: var(--pill-text);
    font-family: "Oswald", sans-serif;
    font-weight: 300;
    text-align: center;
    letter-spacing: 0.18em;
    white-space: nowrap;
  }

  .claims {
    display: flex;
    flex-direction: column;
    align-items: center;
    font-weight: 600;
    line-height: 1.12;
    white-space: nowrap;
  }
  .claim-strength { color: var(--ink); }
  .claim-actives { color: var(--orange-deep); }
  .claim-hyaluronic { color: var(--gold); }
  .claim-natural { color: var(--gold-light); letter-spacing: 0.03em; }
  .volume { font-weight: 400; white-space: nowrap; }

  .box-front .brand { height: 170px; margin-top: 58px; }
  .box-front .brand-dot { width: 46px; height: 46px; }
  .box-front .brand-name { font-size: 24px; }
  .box-front .product-title { font-size: 47px; margin-top: 46px; }
  .box-front .product-pill { width: 200px; font-size: 20px; line-height: 29px; margin-top: 6px; }
  .box-front .claims { margin-top: 168px; }
  .box-front .claim-strength { font-size: 27px; }
  .box-front .claim-actives { font-size: 16px; }
  .box-front .claim-hyaluronic { font-size: 26px; }
  .box-front .claim-natural { font-size: 16px; margin-top: 2px; }
  .box-front .volume { font-size: 17px; margin-top: 56px; }

  /* ---------- Bottle label ---------- */
  .bottle-label {
    width: 300px;
    height: 406px;
    display: flex;
    flex-direction: column;
    background: linear-gradient(90deg, #c4c4c4 0%, #f2f2f2 14%, var(--panel-light) 45%, #f2f2f2 80%, #c4c4c4 100%);
  }
  .bottle-label .band { height: 7px; }
  .label-body {
    flex: 1;
    display: flex;
    flex-direction: column;
    align-items: center;
  }
  .bottle-label .brand { height: 98px; margin-top: 26px; gap: 8px; }
  .bottle-label .brand-dot { width: 30px; height: 30px; }
  .bottle-label .brand-name { font-size: 16px; }
  .bottle-label .product-title { font-size: 46px; margin-top: 22px; }
  .bottle-label .product-pill { width: 160px; font-size: 16px; line-height: 22px; margin-top: 3px; border-radius: 5px; }
  .bottle-label .claims { margin-top: 28px; line-height: 1.1; }
  .bottle-label .claim-strength { font-size: 20px; }
  .bottle-label .claim-actives { font-size: 12px; color: var(--orange); }
  .bottle-label .claim-hyaluronic { font-size: 20px; color: var(--label-gold); }
  .bottle-label .claim-natural { font-size: 12px; color: var(--label-gold); }
  .bottle-label .volume { font-size: 14px; margin-top: 34px; }
</style>
</head>
<body>
  <main class="artboard">
    <section class="box-front" aria-label="Serum box front panel">
      <div class="band band--top"></div>
      <div class="box-body">
        <div class="brand">
          <span class="brand-dot"></span>
          <span class="brand-name">Tidewell Grove</span>
        </div>
        <h1 class="product-title">Vitamin C</h1>
        <div class="product-pill">FACIAL SERUM</div>
        <div class="claims">
          <span class="claim-strength">20% Vitamin C</span>
          <span class="claim-actives">Vitamin E • Organic Aloe</span>
          <span class="claim-hyaluronic">Hyaluronic Acid</span>
          <span class="claim-natural">98% Naturally Derived</span>
        </div>
        <p class="volume">2 Fl oz. (60 ml)</p>
      </div>
      <div class="band band--bottom"></div>
    </section>

    <section class="bottle-label" aria-label="Bottle label">
      <div class="band band--top"></div>
      <div class="label-body">
        <div class="brand">
          <span class="brand-dot"></span>
          <span class="brand-name">Tidewell Grove</span>
        </div>
        <h2 class="product-title">Vitamin C</h2>
        <div class="product-pill">FACIAL SERUM</div>
        <div class="claims">
          <span class="claim-strength">20% Vitamin C</span>
          <span class="claim-actives">Vitamin E • Organic Aloe</span>
          <span class="claim-hyaluronic">Hyaluronic Acid</span>
          <span class="claim-natural">98% Naturally Derived</span>
        </div>
        <p class="volume">2 Fl oz. (60 ml)</p>
      </div>
      <div class="band band--bottom"></div>
    </section>
  </main>
</body>
</html>
```